Cool modern, tech Business card design

Looking for a new business card design for our Managed IT Services company. We would like 2 sides, with the logo one one side horizontally and then the information on the back in either vertical or horizontal. We want our colors from the logo incorporated but also would like to see the color gray in there as well.

Target Market(s)

IT, Information Technology, Tech, Service

Industry/Entity Type

It Service

Contact Information for Business Card

Carl Penner
Managing Partner
(P)555-271-4830 ext xxx
(F)555-271-4831
www.brixtelcore.com

Font styles to use
Sans Serif

Colors
959595
000000
ec1f27

Requirements
Must have
• Logo on one side with some nice design or pattern
• Information on back in either vertical or horizontal format
Nice to have
• For it to look cool, tech, modern, stand out.

```html
<!DOCTYPE html>
<html lang="en">
<head>
<meta charset="utf-8">
<title>Brixtelcore Business Card</title>
<link rel="stylesheet" href="https://fonts.googleapis.com/css2?family=Marcellus&family=Open+Sans:wght@400;600&display=swap">
<style>
  :root {
    --page: #ffffff;
    --ink: #231f20;
    --ink-soft: #5f5f61;
    --red: #ec1f27;
    --red-soft: #d9534a;
    --gray: #959595;
    --card-top: #fafafa;
    --card-bottom: #adadad;
    --strip: #f3f3f3;
  }
  * { margin: 0; padding: 0; box-sizing: border-box; }
  html, body {
    width: 1000px; height: 1200px; overflow: hidden;
    background: var(--page);
  }
  .canvas { position: relative; width: 1000px; height: 1200px; }
  .card {
    position: absolute; left: 33px; width: 934px; height: 531px;
    background: linear-gradient(to bottom, var(--card-top) 0%, #e6e6e6 40%, var(--card-bottom) 100%);
    box-shadow: 6px 8px 10px rgba(0,0,0,0.45);
    overflow: hidden;
  }
  .card--front { top: 46px; }
  .card--back { top: 623px; background: linear-gradient(to bottom, #fafafa 0%, #e4e4e4 50%, #c2c2c2 75%); }

  .brand {
    position: absolute; left: 0; right: 0;
    display: flex; align-items: center; justify-content: center; gap: 16px;
    font-family: "Open Sans", sans-serif; font-weight: 600; letter-spacing: -1px;
  }
  .brand__mark { width: 34px; height: 34px; border-radius: 6px; background: var(--red); }
  .brand--front { top: 230px; font-size: 64px; color: var(--ink); }
  .brand--reflection {
    top: 310px; font-size: 64px; color: var(--ink);
    transform: scaleY(-1); opacity: 0.12;
  }
  .brand--back { top: 295px; font-size: 58px; color: var(--ink-soft); }
  .brand--back .brand__mark { background: var(--red-soft); }

  .person { position: absolute; top: 40px; left: 675px; font-family: "Marcellus", serif; }
  .person__name { font-size: 38px; color: var(--ink); line-height: 1; letter-spacing: 0.5px; }
  .person__role { font-size: 24px; color: var(--red); line-height: 1; margin-left: 10px; }

  .contact-strip {
    position: absolute; left: 2px; right: 2px; top: 404px; height: 114px;
    background: var(--strip);
    box-shadow: inset 0 -6px 6px rgba(0,0,0,0.12), 0 2px 3px rgba(0,0,0,0.2);
    display: flex; align-items: center;
    font-family: "Open Sans", sans-serif; font-size: 20px; color: var(--ink);
  }
  .contact { position: absolute; display: flex; align-items: center; gap: 14px; }
  .contact--phone { left: 75px; }
  .contact--fax { left: 335px; }
  .contact--web { left: 592px; }
  .contact svg { width: 30px; height: 30px; }
</style>
</head>
<body>
<main class="canvas">
  <section class="card card--front" aria-label="Card front">
    <div class="brand brand--front"><span class="brand__name">brixtelcore</span><span class="brand__mark"></span></div>
    <div class="brand brand--reflection" aria-hidden="true"><span class="brand__name">brixtelcore</span><span class="brand__mark"></span></div>
  </section>

  <section class="card card--back" aria-label="Card back">
    <div class="person">
      <p class="person__name">CARL PENNER</p>
      <p class="person__role">Managing Director</p>
    </div>
    <div class="brand brand--back"><span class="brand__name">brixtelcore</span><span class="brand__mark"></span></div>

    <div class="contact-strip">
      <div class="contact contact--phone">
        <svg viewBox="0 0 24 24" fill="none" stroke="#231f20" stroke-width="1.6" stroke-linejoin="round"><path d="M5 3h4l2 5-2.5 1.5a11 11 0 0 0 6 6L16 13l5 2v4a2 2 0 0 1-2 2A16 16 0 0 1 3 5a2 2 0 0 1 2-2z"/></svg>
        <span>555-271-4830</span>
      </div>
      <div class="contact contact--fax">
        <svg viewBox="0 0 24 24" fill="#231f20"><rect x="6" y="2" width="12" height="6"/><rect x="2" y="8" width="20" height="9" rx="2"/><rect x="6" y="13" width="12" height="9" fill="#231f20" stroke="#f3f3f3" stroke-width="1.2"/><path d="M8 16h8M8 19h8" stroke="#f3f3f3" stroke-width="1.2"/></svg>
        <span>555-271-4831</span>
      </div>
      <div class="contact contact--web">
        <svg viewBox="0 0 24 24" fill="none" stroke="#231f20" stroke-width="1.8"><circle cx="12" cy="12" r="10" fill="#231f20"/><g stroke="#f3f3f3" stroke-width="1.2"><ellipse cx="12" cy="12" rx="4.5" ry="10"/><path d="M2 12h20M4 7h16M4 17h16M12 2v20"/></g></svg>
        <span>www.brixtelcore.com</span>
      </div>
    </div>
  </section>
</main>
</body>
</html>
```